Business Cards

Business cards (double-sided) to be handed out to clients and potential clients, with contact details, logo .

Target Market(s)

Small to medium size businesses

Industry/Entity Type

Accountants

Contact Information for Business Card

Brightwater Ledger & Counsel Ltd

Colors

Designer to choose only greyscale colors for use in the design.

Requirements
Must have
• Name, Title, Address, Phone number, Email, Website
Nice to have
• Modern, clean lines, classy
Should not have
• Business cards to be double-sided. Form keeps reverting to single-sided.

```html
<!DOCTYPE html>
<html lang="en">
<head>
<meta charset="utf-8">
<title>Brightwater Ledger &amp; Counsel Ltd — Business Cards</title>
<link href="https://fonts.googleapis.com/css2?family=Jost:wght@300&family=Open+Sans:wght@400;600&display=swap" rel="stylesheet">
<style>
  :root {
    --backdrop: #f1f1f1;
    --card-dark: #505050;
    --card-light: #e9e9e9;
    --ink-light: #ffffff;
    --ink-dark: #4a4a4a;
    --rule: #b9b9b9;
  }
  * { box-sizing: border-box; margin: 0; padding: 0; }
  html, body { width: 1200px; height: 777px; overflow: hidden; background: var(--backdrop); }
  .canvas { position: relative; width: 1200px; height: 777px; }
  .card {
    position: absolute; top: 151px; width: 290px; height: 475px;
    box-shadow: 0 2px 6px rgba(0,0,0,0.12);
  }
  .card--front { left: 290px; background: var(--card-dark); }
  .card--back { left: 620px; background: var(--card-light); color: var(--ink-dark); }

  .front-name {
    position: absolute; left: 50%; top: 50%;
    width: 420px;
    transform: translate(-50%, -50%) rotate(-90deg);
    font-family: "Jost", sans-serif; font-weight: 300;
    font-size: 34px; line-height: 1.15; letter-spacing: 3px;
    text-transform: uppercase; text-align: center;
    color: var(--ink-light);
  }

  .back-name {
    position: absolute; left: 28px; right: 28px; top: 62px;
    font-family: "Jost", sans-serif; font-weight: 300;
    font-size: 22px; line-height: 1.2; letter-spacing: 2px;
    text-transform: uppercase; text-align: right;
    color: var(--ink-dark);
  }

  .company {
    position: absolute; left: 0; right: 0; top: 243px;
    font-family: "Open Sans", sans-serif; font-weight: 600;
    font-size: 11.5px; text-align: center; color: var(--ink-dark);
  }
  .divider {
    position: absolute; left: 14px; right: 12px; top: 272px;
    border-top: 1px solid var(--rule);
  }
  .contacts { position: absolute; left: 36px; top: 286px; list-style: none; }
  .contact {
    display: flex; align-items: flex-start; gap: 22px;
    font-family: "Open Sans", sans-serif; font-size: 11px;
    letter-spacing: 1.3px; color: var(--ink-dark);
    margin-bottom: 10px; min-height: 16px;
  }
  .contact svg { width: 20px; height: 20px; flex: none; fill: none; stroke: var(--ink-dark); }
  .contact--address { font-size: 10px; letter-spacing: 1.4px; line-height: 1.45; text-transform: uppercase; }
</style>
</head>
<body>
<main class="canvas">
  <section class="card card--front" aria-label="Card front">
    <p class="front-name">Brightwater Ledger &amp; Counsel</p>
  </section>

  <section class="card card--back" aria-label="Card back">
    <p class="back-name">Brightwater Ledger &amp; Counsel</p>
    <h1 class="company">Brightwater Ledger &amp; Counsel Ltd</h1>
    <div class="divider"></div>
    <ul class="contacts">
      <li class="contact">
        <svg viewBox="0 0 20 20" aria-hidden="true"><path d="M13 2 l3 3 -3 3 -2-1 -4 6 2 2 -3 3 -3-2 c0-6 6-13 10-14z" fill="#4a4a4a" stroke="none"/></svg>
        <span>+00-0000-0000-00</span>
      </li>
      <li class="contact">
        <svg viewBox="0 0 20 20" aria-hidden="true"><rect x="2" y="5" width="16" height="11" stroke-width="1.4"/><path d="M2 5 l8 6 8-6" stroke-width="1.4"/></svg>
        <span>info@brightwaterledger.com</span>
      </li>
      <li class="contact">
        <svg viewBox="0 0 20 20" aria-hidden="true"><circle cx="10" cy="10" r="8" stroke-width="1.4"/><ellipse cx="10" cy="10" rx="3.5" ry="8" stroke-width="1.2"/><path d="M2 10h16M3.5 6h13M3.5 14h13" stroke-width="1.2"/></svg>
        <span>www.brightwaterledger.com</span>
      </li>
      <li class="contact contact--address">
        <svg viewBox="0 0 20 20" aria-hidden="true"><path d="M10 19 C6 13 4 10 4 7.5 a6 6 0 0 1 12 0 C16 10 14 13 10 19z M10 5 a2.5 2.5 0 1 0 0.01 0z" fill="#4a4a4a" fill-rule="evenodd" stroke="none"/></svg>
        <span>1234 Your Location Here<br>Your Rd. Your Street<br>Postal 0000</span>
      </li>
    </ul>
  </section>
</main>
</body>
</html>
```